Business Card Design Project

Basic business card with minimal details. I just need company name, email & web address, telephone and my name.
I would like the back of the card to be grey with my logo & company name centred.

Target Market(s)

Architects
Builders
Property Developers

Industry/Entity Type

Business

Font styles to use
Sans Serif

Colors

Designer to choose colors to be used in the design.

Requirements
Must have
• Framewise Build
Marcus Helby - Director
M: 0427 593184
E: marcus@framewisebuild.com.au
W: www.framewisebuild.com.au
Should not have
• No other images or pictures

```html
<!DOCTYPE html>
<html lang="en">
<head>
<meta charset="utf-8">
<title>Framewise Build – Business Card</title>
<link rel="stylesheet" href="https://fonts.googleapis.com/css2?family=Raleway:wght@400;500;600&family=Nunito+Sans:wght@300;400&display=swap">
<style>
  :root {
    --page-bg: #e6e7e9;
    --card-front: #ffffff;
    --card-back: #d9dae2;
    --brand-red: #a6123a;
    --brand-slate: #4b5561;
    --text-dark: #1f1f22;
  }
  * { margin: 0; padding: 0; box-sizing: border-box; }
  html, body {
    width: 1200px;
    height: 1200px;
    overflow: hidden;
    background: var(--page-bg);
  }
  .canvas {
    position: relative;
    width: 1200px;
    height: 1200px;
  }
  .card {
    position: absolute;
    left: 174px;
    width: 853px;
    height: 488px;
  }
  .card--front { top: 69px; background: var(--card-front); }
  .card--back  { top: 643px; background: var(--card-back); }

  .brand {
    display: flex;
    align-items: center;
    gap: 12px;
    font-family: "Raleway", sans-serif;
    font-weight: 600;
    color: var(--brand-slate);
    letter-spacing: 0.02em;
    text-transform: uppercase;
    white-space: nowrap;
  }
  .brand__square {
    display: block;
    background: var(--brand-red);
  }
  .card--front .brand {
    position: absolute;
    left: 44px;
    top: 57px;
    font-size: 30px;
  }
  .card--front .brand__square { width: 34px; height: 34px; }

  .person {
    position: absolute;
    left: 45px;
    top: 240px;
  }
  .person__name {
    font-family: "Raleway", sans-serif;
    font-weight: 500;
    font-size: 41px;
    line-height: 46px;
    color: var(--brand-red);
  }
  .person__role {
    font-family: "Raleway", sans-serif;
    font-weight: 400;
    font-size: 26px;
    line-height: 32px;
    color: var(--text-dark);
  }

  .contact {
    position: absolute;
    left: 50px;
    top: 352px;
    font-family: "Nunito Sans", sans-serif;
    font-weight: 300;
    font-size: 25px;
    line-height: 33px;
    color: var(--text-dark);
    list-style: none;
  }
  .contact__row { display: flex; }
  .contact__label { width: 47px; }

  .card--back .brand {
    position: absolute;
    left: 0;
    right: 0;
    top: 275px;
    justify-content: center;
    font-size: 36px;
    gap: 16px;
  }
  .card--back .brand__square { width: 40px; height: 40px; }
</style>
</head>
<body>
<main class="canvas">
  <section class="card card--front" aria-label="Business card front">
    <div class="brand">
      <span class="brand__square" aria-hidden="true"></span>
      <span class="brand__name">Framewise Build</span>
    </div>
    <div class="person">
      <h1 class="person__name">Marcus Helby</h1>
      <p class="person__role">Director</p>
    </div>
    <ul class="contact">
      <li class="contact__row"><span class="contact__label">M:</span><span>0427 593184</span></li>
      <li class="contact__row"><span class="contact__label">E:</span><span>marcus@framewisebuild.com.au</span></li>
      <li class="contact__row"><span class="contact__label">W</span><span>www.framewisebuild.com.au</span></li>
    </ul>
  </section>

  <section class="card card--back" aria-label="Business card back">
    <div class="brand">
      <span class="brand__square" aria-hidden="true"></span>
      <span class="brand__name">Framewise Build</span>
    </div>
  </section>
</main>
</body>
</html>
```